Velvet Shakers business card

We would like a business card designed for our business velvet shakers

We need it to have 2 sides.

More information about the business can be found at www.velvetshakers-example.net

Industry/Entity Type

Business

```html
<!DOCTYPE html>
<html lang="en">
<head>
<meta charset="utf-8">
<title>Velvet Shakers – Business Card</title>
<link href="https://fonts.googleapis.com/css2?family=Arimo:wght@400;700&family=Great+Vibes&display=swap" rel="stylesheet">
<style>
  :root {
    --page: #e9e6e1;
    --card-black: #0b0b0b;
    --gold: #d9c27a;
    --cream: #f7f4c9;
    --text-light: #e8e4d6;
    --icon-bg: #d8d3c0;
    --drink-red: #e8455c;
    --drink-pink: #f7a6b0;
  }
  * { box-sizing: border-box; margin: 0; padding: 0; }
  html, body { width: 1200px; height: 892px; overflow: hidden; }
  body {
    background: var(--page);
    display: flex;
    flex-direction: column;
    align-items: center;
    justify-content: center;
    gap: 36px;
    font-family: "Arimo", Arial, sans-serif;
  }
  .card {
    width: 700px;
    height: 400px;
    position: relative;
    overflow: hidden;
    border-radius: 4px;
    box-shadow: 0 6px 18px rgba(0,0,0,.25);
  }

  /* Front */
  .card--front { background: var(--card-black); }
  .front__info {
    position: absolute; left: 0; top: 0; width: 446px; height: 100%;
    padding: 30px 34px 0 40px;
  }
  .brand-name {
    font-family: "Great Vibes", cursive;
    font-size: 60px;
    color: var(--gold);
    text-align: right;
    line-height: 1;
  }
  .person {
    margin-top: 14px;
    font-family: "Great Vibes", cursive;
    font-size: 38px;
    color: var(--text-light);
    line-height: 1;
  }
  .role {
    margin-top: 6px;
    font-size: 13px;
    color: var(--text-light);
  }
  .contacts {
    list-style: none;
    margin-top: 34px;
    display: flex; flex-direction: column; gap: 8px;
  }
  .contacts li {
    display: flex; align-items: center; gap: 12px;
    font-size: 17px; color: var(--text-light);
  }
  .contact-icon {
    width: 22px; height: 22px; border-radius: 5px;
    background: var(--icon-bg);
    display: flex; align-items: center; justify-content: center;
  }
  .divider {
    position: absolute; left: 446px; top: 0; width: 4px; height: 100%;
    background: var(--gold);
  }
  .front__drink-panel {
    position: absolute; left: 450px; top: 0; right: 0; bottom: 0;
    background: var(--cream);
  }
  .drink-photo {
    position: absolute; left: 60px; top: 70px; width: 130px; height: 280px;
    border-radius: 50% 50% 20% 20% / 30% 30% 10% 10%;
    background: linear-gradient(180deg, #f6b24a 0%, var(--drink-pink) 18%, var(--drink-red) 60%, #dcdcdc 85%, #c8c8c8 100%);
  }

  /* Back */
  .card--back {
    background: var(--card-black);
    display: flex; align-items: center; justify-content: center;
  }
  .card--back .brand-name { font-size: 84px; text-align: center; }
</style>
</head>
<body>

  <section class="card card--front" aria-label="Card front">
    <div class="front__info">
      <p class="brand-name">Velvet Shakers</p>
      <p class="person">Marcus &amp; Dean</p>
      <p class="role">General Manager</p>
      <ul class="contacts">
        <li>
          <span class="contact-icon">
            <svg width="14" height="14" viewBox="0 0 24 24"><path fill="#111" d="M6.6 10.8a15 15 0 0 0 6.6 6.6l2.2-2.2c.3-.3.7-.4 1-.2 1.1.4 2.3.6 3.6.6.6 0 1 .4 1 1V20c0 .6-.4 1-1 1A17 17 0 0 1 3 4c0-.6.4-1 1-1h3.5c.6 0 1 .4 1 1 0 1.3.2 2.5.6 3.6.1.3 0 .7-.2 1z"/></svg>
          </span>0491570156
        </li>
        <li>
          <span class="contact-icon">
            <svg width="14" height="14" viewBox="0 0 24 24"><path fill="#111" d="M6.6 10.8a15 15 0 0 0 6.6 6.6l2.2-2.2c.3-.3.7-.4 1-.2 1.1.4 2.3.6 3.6.6.6 0 1 .4 1 1V20c0 .6-.4 1-1 1A17 17 0 0 1 3 4c0-.6.4-1 1-1h3.5c.6 0 1 .4 1 1 0 1.3.2 2.5.6 3.6.1.3 0 .7-.2 1z"/></svg>
          </span>0491570157
        </li>
        <li>
          <span class="contact-icon">
            <svg width="14" height="14" viewBox="0 0 24 24"><rect x="2" y="5" width="20" height="14" rx="1" fill="none" stroke="#111" stroke-width="2"/><path d="M2 6l10 7 10-7" fill="none" stroke="#111" stroke-width="2"/></svg>
          </span>info@velvetshakers-example.net
        </li>
        <li>
          <span class="contact-icon">
            <svg width="14" height="14" viewBox="0 0 24 24"><circle cx="12" cy="12" r="9" fill="none" stroke="#111" stroke-width="2"/><path d="M3 12h18M12 3c3 3 3 15 0 18M12 3c-3 3-3 15 0 18" fill="none" stroke="#111" stroke-width="1.6"/></svg>
          </span>www.velvetshakers-example.net
        </li>
      </ul>
    </div>
    <div class="divider"></div>
    <div class="front__drink-panel">
      <div class="drink-photo" role="img" aria-label="Photo of a pink cocktail in a tall glass with orange slice and cherry"></div>
    </div>
  </section>

  <section class="card card--back" aria-label="Card back">
    <p class="brand-name">Velvet Shakers</p>
  </section>

</body>
</html>
```